" Fazemos cursos on-line voltados a treinamento de pessoas que querem importar ou exportar. Também damos assessoria para empresas com importações e exportações. "

```html
<!DOCTYPE html>
<html lang="pt-BR">
<head>
<meta charset="utf-8">
<title>Tradevia — Cadernos</title>
<link href="https://fonts.googleapis.com/css2?family=Montserrat:wght@400;500;600;700&display=swap" rel="stylesheet">
<style>
  :root{
    --stage:#1d5a93;
    --navy:#1b4c86;
    --navy-deep:#15406f;
    --orange:#e8832b;
    --white:#ffffff;
    --ink:#2a3a4f;
    --photo-a:#8a95a3;
    --photo-b:#c9ced6;
  }
  html,body{margin:0;padding:0;overflow:hidden;}
  body{
    width:1200px;height:1200px;
    background:radial-gradient(circle at 50% 45%, #2368a6 0%, var(--stage) 55%, #174d80 100%);
    font-family:'Montserrat',sans-serif;
    position:relative;
  }
  .cover{
    position:absolute;top:276px;width:442px;height:648px;
    box-shadow:0 18px 40px rgba(0,0,0,.35);
    overflow:hidden;
  }
  .cover--front{left:125px;background:var(--white);}
  .cover--back{left:653px;background:var(--navy);}
  .cover svg{position:absolute;inset:0;display:block;}
  .course-title{position:absolute;left:22px;bottom:26px;color:var(--white);line-height:1.1;}
  .course-title__kicker{font-size:13px;font-weight:500;display:block;opacity:.9;}
  .course-title__main{font-size:21px;font-weight:600;display:block;}
  .brand{
    position:absolute;left:228px;bottom:132px;display:flex;align-items:center;gap:8px;
    color:var(--navy);font-weight:700;font-size:30px;letter-spacing:-.5px;
  }
  .brand__dot{width:30px;height:30px;border-radius:50%;background:var(--orange);}
  .web{position:absolute;right:22px;top:22px;text-align:right;color:var(--white);font-size:10.5px;line-height:1.6;}
  .address{position:absolute;left:22px;bottom:40px;color:var(--white);font-size:10.5px;line-height:1.5;}
  .contact{position:absolute;right:22px;bottom:40px;color:var(--white);font-size:10.5px;line-height:1.5;text-align:right;}
</style>
</head>
<body>

<section class="cover cover--front">
  <svg width="442" height="648" viewBox="0 0 442 648">
    <defs>
      <linearGradient id="photoFade" x1="0" y1="0" x2="0" y2="1">
        <stop offset="0" stop-color="var(--photo-a)"/>
        <stop offset=".55" stop-color="var(--photo-b)"/>
        <stop offset="1" stop-color="#ffffff"/>
      </linearGradient>
    </defs>
    <rect role="img" aria-label="Foto de dois profissionais analisando documentos em um escritório" x="0" y="0" width="442" height="420" fill="url(#photoFade)"/>
    <circle cx="430" cy="110" r="70" fill="var(--orange)" opacity=".9"/>
    <circle cx="260" cy="230" r="48" fill="var(--orange)" opacity=".85"/>
    <path d="M0 540 C120 520 200 540 442 556 L442 648 L0 648 Z" fill="var(--navy)"/>
  </svg>
  <div class="brand"><span class="brand__dot"></span><span>Tradevia</span></div>
  <div class="course-title">
    <span class="course-title__kicker">Gestão em</span>
    <span class="course-title__main">Comércio Exterior</span>
  </div>
</section>

<section class="cover cover--back">
  <svg width="442" height="648" viewBox="0 0 442 648">
    <path d="M0 0 L442 0 L442 110 C430 88 400 80 360 80 L120 80 C70 80 40 70 20 44 C10 30 4 16 0 0 Z" fill="var(--orange)"/>
    <rect x="0" y="0" width="442" height="10" fill="var(--orange)"/>
    <circle cx="290" cy="340" r="150" fill="var(--navy-deep)" opacity=".45"/>
    <rect x="0" y="636" width="442" height="12" fill="var(--orange)"/>
  </svg>
  <div class="web">www.tradevia.com.br<br>facebook.com/tradevia</div>
  <div class="address">Endereço | Av. Nome | Nº<br>Cidade | CEP | UF | Brasil</div>
  <div class="contact">+00 (00) 0000 0000<br>+00 (00) 0000 0000<br>contato@tradevia.com.br</div>
</section>

</body>
</html>
```